Natural Skin Care e commerce website

we are the distributor for natural skincare product , we would like to develop a e commerce website which encompass the ability to divide the product into face, body , baby , and base on ingredient , best seller, we are Verdel certified product the key point to focus is natural organic , no nasties, vegan , unpolluted , full of natural ingredient. manuka, olive nordic style temporary style website is preferred. the website name is Kolbavi store.co , the web must have ability to take the order and let the brand upload their products

```html
<!DOCTYPE html>
<html lang="en">
<head>
<meta charset="utf-8">
<title>Kolbavi store.co — Natural Skin Care</title>
<link href="https://fonts.googleapis.com/css2?family=Playfair+Display:wght@400;600;700&family=Poppins:wght@300;400;500;600&display=swap" rel="stylesheet">
<style>
:root{
  --bg:#ecebe2;
  --bg-soft:#f3f2ea;
  --forest:#1d3a24;
  --green:#2d5a33;
  --leaf:#4d7a45;
  --leaf-light:#8db07a;
  --ink:#2a2a26;
  --muted:#6d6c64;
  --line:#d5d3c6;
  --white:#ffffff;
  --gold:#e2b33c;
  --footer:#111512;
}
*{margin:0;padding:0;box-sizing:border-box}
html,body{width:1200px;height:4512px;overflow:hidden}
body{background:var(--bg);font-family:'Poppins',sans-serif;color:var(--ink);position:relative}
section,header{position:absolute;left:0;width:1200px}
.btn{display:inline-block;background:var(--forest);color:var(--white);font-size:13px;font-weight:500;letter-spacing:1px;padding:12px 26px;text-transform:uppercase}
.section-title{font-family:'Playfair Display',serif;font-size:38px;font-weight:600;color:var(--green);text-align:center}
.section-sub{font-size:15px;color:var(--muted);text-align:center;margin-top:10px}
.ph{position:absolute}
.leaf-r{background:linear-gradient(135deg,#2f6a31,#5b8f45);opacity:.85}
.leaf-l{background:linear-gradient(135deg,#5b8f45,#2f6a31);opacity:.85}

/* top bar */
.topbar{top:0;height:48px;background:var(--forest);color:var(--white);font-size:12px;letter-spacing:.5px;display:flex;align-items:center;justify-content:space-between;padding:0 40px}
.topbar span{display:flex;align-items:center;gap:8px}
/* nav */
.nav{top:48px;height:72px;background:var(--bg);display:flex;align-items:center;justify-content:space-between;padding:0 110px}
.nav-links{display:flex;gap:38px;font-size:14px}
.logo{font-family:'Playfair Display',serif;font-weight:700;font-size:32px;letter-spacing:2px;color:var(--ink)}
.nav-right{display:flex;gap:34px;align-items:center;font-size:14px}
.nav-icons{display:flex;gap:14px}
/* hero */
.hero{top:120px;height:600px;background:linear-gradient(120deg,#163c1f 0%,#2f6a31 35%,#4d8a3e 60%,#1f4a25 100%)}
.hero-copy{position:absolute;left:110px;top:190px;color:var(--white)}
.hero-copy h1{font-family:'Playfair Display',serif;font-weight:400;font-size:46px;line-height:1.12}
.hero-copy .btn{margin-top:30px;background:transparent;border:1px solid var(--white);padding:8px 16px;font-size:12px}
.hero-bottles{left:650px;top:40px;width:320px;height:400px;background:linear-gradient(180deg,#5a3a2a,#2b1a14);border-radius:18px;opacity:.9}
.seal{left:870px;top:80px;width:90px;height:90px;border-radius:50%;background:var(--forest);border:2px solid var(--white)}
/* categories */
.categories{top:720px;height:520px}
.cat-grid{position:absolute;top:192px;left:112px;display:flex;gap:74px}
.cat{width:254px;text-align:center}
.cat .img{height:244px;width:254px}
.cat p{font-family:'Playfair Display',serif;font-size:20px;margin-top:20px}
/* featured */
.featured{top:1240px;height:620px;border-top:1px solid var(--line)}
.products{position:absolute;top:170px;left:130px;display:flex;gap:68px}
.product{width:268px}
.product .img{height:310px;background:linear-gradient(180deg,#f7f6f0,#e3e1d6);position:relative}
.product .bottle{position:absolute;left:98px;top:36px;width:72px;height:244px;border-radius:12px 12px 8px 8px;background:linear-gradient(90deg,#3a2317,#6a4028,#2c1a11)}
.product h3{font-size:14px;font-weight:500;margin-top:20px}
.product .meta{font-size:10px;color:var(--muted);margin-top:4px;letter-spacing:.5px}
.product .row{display:flex;justify-content:space-between;align-items:center;margin-top:14px;font-size:14px}
.product .row .btn{font-size:12px;padding:8px 18px}
.product .row .ghost{font-size:12px;letter-spacing:.5px;padding:8px 18px}
.arrow{position:absolute;width:30px;height:30px;border-radius:50%;background:var(--forest);display:flex;align-items:center;justify-content:center}
/* ingredients */
.ingredients{top:1860px;height:470px;border-top:1px solid var(--line)}
.badges{position:absolute;top:200px;left:110px;display:flex;gap:50px}
.badge{width:120px;height:120px;border-radius:50%;border:1px solid var(--leaf-light);display:flex;flex-direction:column;align-items:center;justify-content:center;gap:6px;background:var(--bg-soft)}
.badge span{font-size:10px;font-weight:500;letter-spacing:1px;color:var(--green);text-transform:uppercase}
/* testimonial */
.testimonial{top:2330px;height:550px;border-top:1px solid var(--line)}
.quote{position:absolute;top:180px;left:170px;width:860px;text-align:center;font-size:13px;line-height:2;color:var(--muted);font-style:italic}
.stars{position:absolute;top:300px;left:0;width:1200px;display:flex;justify-content:center;gap:4px}
.avatars{position:absolute;top:328px;left:0;width:1200px;display:flex;justify-content:center;gap:26px;align-items:center}
.avatar{border-radius:50%;background:linear-gradient(160deg,#d9c3ad,#9d7a5e);border:3px solid var(--bg-soft)}
.t-name{position:absolute;top:412px;left:0;width:1200px;text-align:center;font-size:13px;font-weight:600;letter-spacing:1px}
/* why */
.why{top:2880px;height:540px;border-top:1px solid var(--line)}
.why-img{left:0;top:20px;width:600px;height:500px;background:linear-gradient(135deg,#4f7a3c,#c9b79a 55%,#e8e2d2)}
.why-bottle{left:350px;top:110px;width:130px;height:330px;border-radius:16px;background:linear-gradient(90deg,#3a2317,#7a4a2d,#2c1a11)}
.why-copy{position:absolute;left:640px;top:60px;width:460px}
.why-copy h2{font-family:'Playfair Display',serif;font-size:34px;font-weight:600;color:var(--green)}
.why-copy .lead{font-size:14px;color:var(--muted);margin-top:14px;line-height:1.6}
.why-copy ul{list-style:none;margin-top:18px}
.why-copy li{display:flex;gap:10px;align-items:center;font-size:11px;color:var(--muted);margin-bottom:9px}
.why-badges{display:flex;gap:22px;margin-top:20px}
.mini-badge{width:64px;height:64px;border-radius:50%;border:1px solid var(--leaf-light);background:var(--bg-soft)}
/* instagram */
.insta{top:3420px;height:440px;border-top:1px solid var(--line)}
.insta-grid{position:absolute;top:150px;left:112px;display:flex;gap:20px}
.insta-grid div{width:230px;height:230px}
/* newsletter */
.newsletter{top:3860px;height:340px;background:linear-gradient(90deg,#1c3c1a,#3f6e2a 20%,#5d8c35 40%,#2f5a22 60%,#6a9a3c 80%,#1f4020);color:var(--white);text-align:center}
.newsletter .logo{color:var(--white);position:absolute;top:88px;left:0;width:1200px;text-align:center}
.newsletter p{position:absolute;top:140px;left:0;width:1200px;font-size:15px}
.signup{position:absolute;top:186px;left:340px;display:flex}
.signup .input{width:420px;height:44px;background:var(--white);color:var(--muted);font-size:12px;text-align:left;padding:14px 18px}
.signup .btn{height:44px;padding:14px 22px}
/* footer */
.footer{position:absolute;left:0;width:1200px;top:4200px;height:312px;background:var(--footer);color:#d8d8d2}
.footer .logo{color:var(--white);position:absolute;left:112px;top:40px}
.socials{position:absolute;left:112px;top:110px;display:flex;gap:14px}
.socials span{width:34px;height:34px;border-radius:50%;border:1px solid #555;display:block}
.fcol{position:absolute;top:50px;font-size:12px;line-height:1.9}
.fcol h4{font-size:13px;font-weight:600;color:var(--white);margin-bottom:6px;letter-spacing:1px}
.fcol .ci{display:flex;gap:8px;align-items:center}
.copyright{position:absolute;top:264px;left:0;width:1200px;text-align:center;font-size:12px;color:#9a9a94;border-top:1px solid #2a2e2b;padding-top:14px}
</style>
</head>
<body>

<header class="topbar">
  <span><svg width="14" height="14" viewBox="0 0 14 14"><circle cx="7" cy="7" r="6" fill="none" stroke="#fff"/><path d="M4 7l2 2 4-4" stroke="#fff" fill="none"/></svg>MONEY GUARANTEE</span>
  <span><svg width="18" height="14" viewBox="0 0 18 14"><rect x="1" y="2" width="10" height="8" fill="none" stroke="#fff"/><path d="M11 5h4l2 3v2h-6z" fill="none" stroke="#fff"/><circle cx="5" cy="11" r="1.5" fill="#fff"/><circle cx="14" cy="11" r="1.5" fill="#fff"/></svg>FREE SHIPPING ON ORDER OVER $50</span>
  <span><svg width="14" height="14" viewBox="0 0 14 14"><path d="M3 1l3 3-2 2c1 2 2 3 4 4l2-2 3 3-2 2C6 13 1 8 1 3z" fill="#fff"/></svg>CALL US 1 800 555 0142</span>
</header>

<header class="nav">
  <nav class="nav-links"><span>Our products</span><span>About Us</span><span>Learn</span></nav>
  <div class="logo">KOLBAVI</div>
  <div class="nav-right">
    <span>Contact Us</span><span>FAQ</span>
    <div class="nav-icons">
      <svg width="16" height="16" viewBox="0 0 16 16"><circle cx="7" cy="7" r="5" fill="none" stroke="#2a2a26" stroke-width="1.5"/><path d="M11 11l4 4" stroke="#2a2a26" stroke-width="1.5"/></svg>
      <svg width="16" height="16" viewBox="0 0 16 16"><circle cx="8" cy="5" r="3" fill="none" stroke="#2a2a26" stroke-width="1.5"/><path d="M2 15c0-4 12-4 12 0" fill="none" stroke="#2a2a26" stroke-width="1.5"/></svg>
      <svg width="16" height="16" viewBox="0 0 16 16"><path d="M8 14L2 8a3 3 0 016-4 3 3 0 016 4z" fill="none" stroke="#2a2a26" stroke-width="1.5"/></svg>
      <svg width="16" height="16" viewBox="0 0 16 16"><path d="M1 2h3l2 9h8l1-6H5" fill="none" stroke="#2a2a26" stroke-width="1.5"/><circle cx="7" cy="14" r="1.2" fill="#2a2a26"/><circle cx="13" cy="14" r="1.2" fill="#2a2a26"/></svg>
    </div>
  </div>
</header>

<section class="hero" role="img" aria-label="Large tropical green leaves with two amber dropper bottles of skin care serum">
  <div class="ph hero-bottles" role="img" aria-label="Two amber serum bottles with droppers"></div>
  <div class="ph seal" role="img" aria-label="Round natural product seal"></div>
  <div class="hero-copy">
    <h1>All Natural<br>Cosmetics &amp; Personal<br>Skin Care Products.</h1>
    <span class="btn">Browse Product</span>
  </div>
</section>

<section class="categories">
  <div class="ph leaf-r" style="left:1080px;top:20px;width:120px;height:150px;border-radius:80px 0 0 80px" role="img" aria-label="Palm leaf decoration"></div>
  <h2 class="section-title" style="margin-top:84px">Shop by Categories</h2>
  <p class="section-sub">Lorem ipsum dolor sit amet, consectetur adipiscing elit.</p>
  <div class="cat-grid">
    <div class="cat"><div class="img" style="background:linear-gradient(160deg,#e9e4da,#c9b6a1)" role="img" aria-label="Woman with towel applying face care"></div><p>Face Product</p></div>
    <div class="cat"><div class="img" style="background:linear-gradient(160deg,#efe6dc,#d2b49d)" role="img" aria-label="Woman applying body lotion"></div><p>Body Product</p></div>
    <div class="cat"><div class="img" style="background:linear-gradient(160deg,#f1ece4,#cdb8a5)" role="img" aria-label="Baby receiving gentle skin care"></div><p>Baby Product</p></div>
  </div>
</section>

<section class="featured">
  <div class="ph leaf-l" style="left:0;top:16px;width:100px;height:140px;border-radius:0 80px 80px 0" role="img" aria-label="Palm leaf decoration"></div>
  <h2 class="section-title" style="margin-top:44px">Our Featured Product</h2>
  <p class="section-sub">Lorem ipsum dolor sit amet, consectetur adipiscing elit.</p>
  <div class="arrow" style="left:80px;top:420px"><svg width="10" height="10" viewBox="0 0 10 10"><path d="M7 1L3 5l4 4" stroke="#fff" fill="none" stroke-width="1.5"/></svg></div>
  <div class="arrow" style="left:1090px;top:420px"><svg width="10" height="10" viewBox="0 0 10 10"><path d="M3 1l4 4-4 4" stroke="#fff" fill="none" stroke-width="1.5"/></svg></div>
  <div class="products">
    <div class="product">
      <div class="img"><div class="bottle" role="img" aria-label="Amber pump bottle"></div></div>
      <h3>PRODUCT NAME LOREM</h3><div class="meta">GENTLE NATURAL SERUM</div>
      <div class="row"><span>$55.0</span><span class="ghost">ADD TO CART</span></div>
    </div>
    <div class="product">
      <div class="img"><div class="bottle" style="width:62px;left:103px" role="img" aria-label="Tall amber pump bottle"></div></div>
      <h3>PRODUCT NAME LOREM</h3><div class="meta">GENTLE NATURAL SERUM</div>
      <div class="row"><span>$55.0</span><span class="btn">ADD TO CART</span></div>
    </div>
    <div class="product">
      <div class="img"><div class="bottle" style="top:86px;height:194px;width:80px;left:94px" role="img" aria-label="Amber dropper bottle"></div></div>
      <h3>PRODUCT NAME LOREM</h3><div class="meta">GENTLE NATURAL SERUM</div>
      <div class="row"><span>$55.0</span><span class="ghost">ADD TO CART</span></div>
    </div>
  </div>
</section>

<section class="ingredients">
  <div class="ph leaf-r" style="left:1110px;top:30px;width:90px;height:140px;border-radius:80px 0 0 80px" role="img" aria-label="Palm leaf decoration"></div>
  <div class="ph leaf-l" style="left:0;top:345px;width:80px;height:110px;border-radius:0 70px 70px 0" role="img" aria-label="Palm leaf decoration"></div>
  <h2 class="section-title" style="margin-top:100px">100% Natural Organic Ingredient</h2>
  <div class="badges">
    <div class="badge"><span>Natural Organic</span><svg width="34" height="34" viewBox="0 0 34 34"><path d="M17 30C6 24 6 10 17 4c11 6 11 20 0 26zM17 30V10" fill="none" stroke="#4d7a45" stroke-width="1.5"/></svg></div>
    <div class="badge"><span>No Nasties</span><svg width="34" height="34" viewBox="0 0 34 34"><path d="M17 4c6 8 10 13 10 18a10 10 0 01-20 0c0-5 4-10 10-18z" fill="none" stroke="#4d7a45" stroke-width="1.5"/></svg></div>
    <div class="badge"><span>Vegan</span><svg width="34" height="34" viewBox="0 0 34 34"><path d="M6 8l11 20L28 8" fill="none" stroke="#4d7a45" stroke-width="1.5"/></svg></div>
    <div class="badge"><span>Unpolluted</span><svg width="34" height="34" viewBox="0 0 34 34"><path d="M4 24l9-12 6 8 4-5 7 9z" fill="none" stroke="#4d7a45" stroke-width="1.5"/></svg></div>
    <div class="badge"><span>Manuka</span><svg width="34" height="34" viewBox="0 0 34 34"><circle cx="17" cy="17" r="5" fill="none" stroke="#4d7a45" stroke-width="1.5"/><circle cx="17" cy="8" r="4" fill="none" stroke="#4d7a45"/><circle cx="17" cy="26" r="4" fill="none" stroke="#4d7a45"/><circle cx="8" cy="17" r="4" fill="none" stroke="#4d7a45"/><circle cx="26" cy="17" r="4" fill="none" stroke="#4d7a45"/></svg></div>
    <div class="badge"><span>Olive</span><svg width="34" height="34" viewBox="0 0 34 34"><ellipse cx="17" cy="20" rx="7" ry="9" fill="none" stroke="#4d7a45" stroke-width="1.5"/><path d="M17 11c2-4 6-6 10-6" fill="none" stroke="#4d7a45" stroke-width="1.5"/></svg></div>
  </div>
  <div style="position:absolute;top:378px;left:0;width:1200px;text-align:center"><span class="btn">Discover Product</span></div>
</section>

<section class="testimonial">
  <h2 class="section-title" style="margin-top:66px">Client Testimonial</h2>
  <p class="section-sub">Lorem ipsum dolor sit amet, consectetur adipiscing elit.</p>
  <div class="arrow" style="left:80px;top:200px"><svg width="10" height="10" viewBox="0 0 10 10"><path d="M7 1L3 5l4 4" stroke="#fff" fill="none" stroke-width="1.5"/></svg></div>
  <div class="arrow" style="left:1090px;top:200px"><svg width="10" height="10" viewBox="0 0 10 10"><path d="M3 1l4 4-4 4" stroke="#fff" fill="none" stroke-width="1.5"/></svg></div>
  <p class="quote">My skin has never felt this calm. The serum is light, soaks in quickly and leaves no heavy film behind. I love knowing every bottle is made from clean plant ingredients, and my whole family now uses the body and baby range every single day. Delivery was fast and the packaging was fully recyclable too.</p>
  <div class="stars">
    <svg width="100" height="18" viewBox="0 0 100 18"><g fill="#e2b33c"><path id="st" d="M9 1l2.4 5 5.4.6-4 3.7 1.1 5.3L9 13 4.1 15.6l1.1-5.3-4-3.7 5.4-.6z"/><use href="#st" x="20"/><use href="#st" x="40"/><use href="#st" x="60"/><use href="#st" x="80"/></g></svg>
  </div>
  <div class="avatars">
    <div class="avatar" style="width:52px;height:52px;opacity:.7" role="img" aria-label="Customer portrait"></div>
    <div class="avatar" style="width:70px;height:70px" role="img" aria-label="Portrait of reviewer"></div>
    <div class="avatar" style="width:52px;height:52px;opacity:.7" role="img" aria-label="Customer portrait"></div>
  </div>
  <div class="t-name">LENA MORAVEC</div>
  <div style="position:absolute;top:460px;left:0;width:1200px;text-align:center"><span class="btn">View All Reviews</span></div>
</section>

<section class="why">
  <div class="ph why-img" role="img" aria-label="Green leaves, towels and flowers arranged with skin care bottles"></div>
  <div class="ph why-bottle" role="img" aria-label="Amber pump bottle of body wash"></div>
  <div class="why-copy">
    <h2>Why All Natural Ingredient ?</h2>
    <p class="lead">Be simple, then be comfortable.<br>Kolbavi makes your skin comfortable and relaxed.</p>
    <ul>
      <li><svg width="12" height="12" viewBox="0 0 12 12"><path d="M1 6l3 3 7-7" stroke="#2d5a33" fill="none" stroke-width="1.6"/></svg>Pure plant extracts, gently cold pressed for daily use.</li>
      <li><svg width="12" height="12" viewBox="0 0 12 12"><path d="M1 6l3 3 7-7" stroke="#2d5a33" fill="none" stroke-width="1.6"/></svg>No parabens, sulfates or synthetic fragrance added.</li>
      <li><svg width="12" height="12" viewBox="0 0 12 12"><path d="M1 6l3 3 7-7" stroke="#2d5a33" fill="none" stroke-width="1.6"/></svg>Vegan formulas, never tested on any animals.</li>
      <li><svg width="12" height="12" viewBox="0 0 12 12"><path d="M1 6l3 3 7-7" stroke="#2d5a33" fill="none" stroke-width="1.6"/></svg>Manuka honey and olive oil for deep hydration.</li>
      <li><svg width="12" height="12" viewBox="0 0 12 12"><path d="M1 6l3 3 7-7" stroke="#2d5a33" fill="none" stroke-width="1.6"/></svg>Gentle enough for baby and sensitive skin types.</li>
    </ul>
    <div class="why-badges"><div class="mini-badge"></div><div class="mini-badge"></div><div class="mini-badge"></div><div class="mini-badge"></div></div>
    <div style="margin-top:24px"><span class="btn">Discover More</span></div>
  </div>
  <div class="ph leaf-r" style="left:1120px;top:320px;width:80px;height:170px;border-radius:80px 0 0 80px" role="img" aria-label="Palm leaf decoration"></div>
</section>

<section class="insta">
  <h2 class="section-title" style="margin-top:44px">Follow Us On Instagram</h2>
  <p class="section-sub">Lorem ipsum dolor sit amet, consectetur adipiscing elit.</p>
  <div class="insta-grid">
    <div style="background:linear-gradient(160deg,#e6d2c0,#a9826a)" role="img" aria-label="Woman holding a skin care tube"></div>
    <div style="background:linear-gradient(160deg,#3f6b32,#8a6a50)" role="img" aria-label="Woman posing among green leaves"></div>
    <div style="background:linear-gradient(160deg,#d8cfc4,#7b6a5e)" role="img" aria-label="Woman smiling with towel"></div>
    <div style="background:linear-gradient(160deg,#f3ece3,#d6bca6)" role="img" aria-label="Baby wrapped in a soft towel"></div>
  </div>
</section>

<section class="newsletter" role="img" aria-label="Green bamboo stalks background">
  <div class="logo">KOLBAVI</div>
  <p>Sign up to get 20% off on Next Order</p>
  <div class="signup"><div class="input">Email Address</div><span class="btn">Sign Up</span></div>
</section>

<footer class="footer">
  <div class="logo">KOLBAVI</div>
  <div class="socials"><span></span><span></span><span></span></div>
  <div class="fcol" style="left:420px"><h4>NAVIGATION</h4>Home<br>About<br>Learn<br>Faqs<br>Contact us</div>
  <div class="fcol" style="left:650px"><h4>CONTACT US</h4>
    <div class="ci"><svg width="10" height="12" viewBox="0 0 10 12"><path d="M5 11S1 7 1 4.5a4 4 0 018 0C9 7 5 11 5 11z" fill="#d8d8d2"/></svg>88 Linden Crescent, Unit 2</div>
    <div class="ci" style="padding-left:18px">Harlow Bay, OR 97001</div>
    <div class="ci"><svg width="10" height="10" viewBox="0 0 14 14"><path d="M3 1l3 3-2 2c1 2 2 3 4 4l2-2 3 3-2 2C6 13 1 8 1 3z" fill="#d8d8d2"/></svg>1 800 555 0142</div>
    <div class="ci"><svg width="10" height="10" viewBox="0 0 14 14"><path d="M3 1l3 3-2 2c1 2 2 3 4 4l2-2 3 3-2 2C6 13 1 8 1 3z" fill="#d8d8d2"/></svg>1 800 555 0143</div>
    <div class="ci"><svg width="12" height="9" viewBox="0 0 12 9"><rect x=".5" y=".5" width="11" height="8" fill="none" stroke="#d8d8d2"/><path d="M.5.5L6 5l5.5-4.5" fill="none" stroke="#d8d8d2"/></svg>hello@kolbavi.co</div>
  </div>
  <div class="fcol" style="left:930px"><h4>RESOURCES</h4>Blog<br>Newsletter<br>FAQs<br>Compensation Disclosure</div>
  <div class="copyright">Copyright © 2020 KOLBAVI . All Rights Reserved.</div>
</footer>

</body>
</html>
```